Envelope design

We need a envelope design for a professional services firm called Brindlemoor Tax Consultancy Inc. The firm is essentially a very specialized tax accounting firm - instead of serving the end consumer, we support other public accounting firms in the area of Canadian and U.S. tax advisory and compliance (i.e. they call us on tax issues too complex for the general practitioner). Our byline is "Tax Support Services for Public Accounting Firms". Our postcard should utilize our logo and be based on colours present in our logo (see file attached). The final design needs to convey professionalism and trustworthiness (we're hired by accountants after all!) while being creative and eye-catching. Eye-catching is critical, since many prospective recipients will not have heard from me before and I want them to read the postcard.
At lot of design work has already been done here. I've attached a number of sample files showing logo and letterhead designs. Please note that the letterhead hasn't yet been updated for the new logo. This is happening in a separate design competition.
Updates
Project Deadline Extended Reason: Deadline is extended because I am pricing the extra cost of having colour right to the edge of the envelopes. This will help me design on final design. Pricing should come in on Monday. Added Saturday, February 20, 2016

```html
<!DOCTYPE html>
<html lang="en">
<head>
<meta charset="utf-8">
<title>Brindlemoor Tax Consultancy – Stationery</title>
<link href="https://fonts.googleapis.com/css2?family=Open+Sans:wght@400;600&display=swap" rel="stylesheet">
<style>
  :root {
    --board-light: #14b592;
    --board-dark: #0a7a64;
    --ink: #231f20;
    --paper: #ffffff;
    --orange: #f7941d;
    --red-orange: #ef4b23;
    --gold: #f6b92b;
    --name-grey: #3a3a3a;
    --tag-grey: #8a8a8a;
    --fold-grey: #d4d4d4;
  }
  * { margin: 0; padding: 0; box-sizing: border-box; }
  html, body { width: 1200px; height: 762px; overflow: hidden; }
  body {
    position: relative;
    background: radial-gradient(ellipse at 45% 40%, var(--board-light), var(--board-dark));
    font-family: "Open Sans", Arial, sans-serif;
  }
  .piece { position: absolute; background: var(--paper); overflow: hidden; box-shadow: 0 2px 6px rgba(0,0,0,.35); }

  /* firm name block */
  .brand { position: absolute; display: flex; align-items: center; gap: 8px; }
  .brand-dot { width: 22px; height: 22px; border-radius: 50%; background: var(--orange); flex: none; }
  .brand-name { font-weight: 600; color: var(--name-grey); white-space: nowrap; line-height: 1.1; }
  .strapline { position: absolute; color: var(--tag-grey); white-space: nowrap; line-height: 1; }

  .rule { position: absolute; left: 0; right: 0; background: linear-gradient(90deg, var(--red-orange), var(--orange)); }
  .band { position: absolute; left: 0; right: 0; bottom: 0; background: var(--ink); }
  .label { color: var(--gold); font-weight: 600; }
  .label-red { color: var(--red-orange); font-weight: 600; }

  /* letterhead */
  .letterhead { left: 30px; top: 20px; width: 511px; height: 722px; }
  .letterhead .brand { left: 24px; top: 30px; }
  .letterhead .brand-name { font-size: 17px; }
  .letterhead .strapline { left: 54px; top: 55px; font-size: 9px; }
  .letterhead .rule { top: 670px; height: 4px; }
  .letterhead .band { height: 48px; }
  .lh-contact { position: absolute; top: 12px; font-size: 10px; line-height: 13px; color: #fff; }
  .lh-phones { left: 28px; }
  .lh-online { left: 111px; padding-left: 10px; border-left: 1px solid var(--orange); }

  /* business cards */
  .card-front { left: 584px; top: 20px; width: 221px; height: 126px; }
  .card-front .band { top: 0; bottom: auto; height: 82px; }
  .card-front .brand { left: 18px; top: 50px; gap: 5px; }
  .card-front .brand-dot { width: 12px; height: 12px; }
  .card-front .brand-name { font-size: 8px; color: #fff; }
  .card-front .strapline { left: 35px; top: 65px; font-size: 4.5px; color: #bbb; }
  .card-url { position: absolute; left: 0; right: 0; top: 106px; text-align: center; font-size: 8px; font-weight: 600; color: var(--red-orange); }

  .card-back { left: 821px; top: 20px; width: 222px; height: 126px; }
  .card-back .brand { left: 24px; top: 22px; gap: 5px; }
  .card-back .brand-dot { width: 12px; height: 12px; }
  .card-back .brand-name { font-size: 8px; }
  .card-back .strapline { left: 41px; top: 36px; font-size: 4.5px; }
  .card-back .rule { top: 64px; height: 3px; }
  .card-back .band { height: 59px; }
  .cb-contact { position: absolute; left: 13px; top: 17px; font-size: 5.6px; line-height: 8.5px; color: #fff; }
  .cb-name { position: absolute; left: 128px; top: 14px; font-size: 12.5px; color: var(--gold); }

  /* envelope back */
  .envelope-back { left: 584px; top: 170px; width: 584px; height: 276px; }
  .envelope-back svg { position: absolute; inset: 0; }

  /* envelope front */
  .envelope-front { left: 584px; top: 467px; width: 584px; height: 276px; }
  .envelope-front .brand { left: 24px; top: 42px; }
  .envelope-front .brand-name { font-size: 17px; }
  .envelope-front .strapline { left: 54px; top: 67px; font-size: 9px; }
  .ef-contact { position: absolute; left: 24px; top: 182px; font-size: 10px; line-height: 12.5px; color: var(--ink); }
  .envelope-front .rule { top: 231px; height: 5px; }
  .envelope-front .band { height: 40px; }
  .ef-url { position: absolute; right: 66px; top: 13px; font-size: 10px; font-weight: 600; color: var(--gold); }
</style>
</head>
<body>

<section class="piece letterhead">
  <div class="brand">
    <span class="brand-dot"></span>
    <span class="brand-name">BRINDLEMOOR TAX CONSULTANCY</span>
  </div>
  <div class="strapline">Specialist tax advice for accounting practices</div>
  <div class="rule"></div>
  <div class="band">
    <div class="lh-contact lh-phones"><span class="label">P:</span> 902.555.0148<br><span class="label">F</span> : 902.555.0172</div>
    <div class="lh-contact lh-online">dana@brindlemoortax.ca<br>www.brindlemoortax.ca</div>
  </div>
</section>

<section class="piece card-front">
  <div class="band"></div>
  <div class="brand">
    <span class="brand-dot"></span>
    <span class="brand-name">BRINDLEMOOR TAX CONSULTANCY</span>
  </div>
  <div class="strapline">Specialist tax advice for accounting practices</div>
  <div class="card-url">www.brindlemoortax.ca</div>
</section>

<section class="piece card-back">
  <div class="brand">
    <span class="brand-dot"></span>
    <span class="brand-name">BRINDLEMOOR TAX CONSULTANCY</span>
  </div>
  <div class="strapline">Specialist tax advice for accounting practices</div>
  <div class="rule"></div>
  <div class="band">
    <div class="cb-contact">
      <span class="label">P</span> : 902.555.0148<br>
      <span class="label">F</span> : 902.555.0172<br>
      <span class="label">E</span> : dana@brindlemoortax.ca<br>
      <span class="label">W</span> : www.brindlemoortax.ca
    </div>
    <div class="cb-name">Owen Marsh</div>
  </div>
</section>

<section class="piece envelope-back">
  <svg width="584" height="276" viewBox="0 0 584 276">
    <line x1="150" y1="96" x2="12" y2="270" stroke="var(--fold-grey)" stroke-width="1.2"/>
    <line x1="436" y1="96" x2="574" y2="270" stroke="var(--fold-grey)" stroke-width="1.2"/>
    <path d="M0 0 H584 C580 14 576 22 566 28 L310 112 Q292 118 274 112 L18 28 C8 22 4 14 0 0 Z" fill="var(--ink)"/>
  </svg>
</section>

<section class="piece envelope-front">
  <div class="brand">
    <span class="brand-dot"></span>
    <span class="brand-name">BRINDLEMOOR TAX CONSULTANCY</span>
  </div>
  <div class="strapline">Specialist tax advice for accounting practices</div>
  <div class="ef-contact">
    <span class="label-red">P</span> : 902.555.0148<br>
    <span class="label-red">F</span> : 902.555.0172<br>
    <span class="label-red">E</span> : dana@brindlemoortax.ca
  </div>
  <div class="rule"></div>
  <div class="band">
    <div class="ef-url">www.BrindlemoorTax.ca</div>
  </div>
</section>

</body>
</html>
```